Business Card Design Project

Financial planning, Insurance and Real estate - Financial Services company

Contact Information for Business Card

Looking for something simple in design -
Tolverin Equity LLC
Tolverin Wealth Managment

```html
<!DOCTYPE html>
<html lang="en">
<head>
<meta charset="utf-8">
<title>Tolverin Wealth Management – Business Card</title>
<link rel="stylesheet" href="https://fonts.googleapis.com/css2?family=Roboto+Condensed:wght@400;700&display=swap">
<style>
  :root {
    --stage: #e9e6e1;
    --card-white: #ffffff;
    --card-shade: #eef0f2;
    --brand-blue: #1a95c8;
    --brand-blue-deep: #0f74ad;
    --brand-blue-light: #45bde0;
    --text-white: #ffffff;
  }
  * { margin: 0; padding: 0; box-sizing: border-box; }
  html, body { width: 1200px; height: 1023px; overflow: hidden; }
  body {
    background: var(--stage);
    font-family: "Roboto Condensed", sans-serif;
    position: relative;
  }
  .card {
    position: absolute;
    left: 250px;
    width: 700px;
    height: 400px;
    border-radius: 22px;
    overflow: hidden;
    background: linear-gradient(160deg, var(--card-white) 40%, var(--card-shade));
    box-shadow: 0 10px 26px rgba(0,0,0,0.18);
  }
  .card--front { top: 81px; }
  .card--back { top: 542px; }
  .card__art { position: absolute; inset: 0; width: 100%; height: 100%; }

  .brand {
    position: absolute;
    display: flex;
    align-items: center;
    gap: 12px;
    color: var(--brand-blue);
    font-weight: 700;
    white-space: nowrap;
  }
  .brand__dot {
    width: 26px; height: 26px;
    border-radius: 50%;
    background: var(--brand-blue);
    flex: none;
  }
  .card--front .brand { top: 70px; right: 50px; font-size: 26px; }
  .card--back .brand {
    top: 50%; left: 50%;
    transform: translate(-50%, -50%);
    font-size: 34px; gap: 16px;
  }
  .card--back .brand__dot { width: 32px; height: 32px; }

  .holder {
    position: absolute;
    left: 44px;
    top: 274px;
    color: var(--text-white);
    white-space: nowrap;
  }
  .holder__name {
    font-size: 34px;
    font-weight: 700;
    letter-spacing: 0.5px;
    line-height: 1;
  }
  .holder__role { font-size: 17px; margin-top: 6px; }

  .contacts {
    position: absolute;
    left: 400px;
    top: 280px;
    list-style: none;
    color: var(--text-white);
    font-size: 18px;
    white-space: nowrap;
  }
  .contacts li {
    display: flex;
    align-items: center;
    gap: 10px;
    height: 28px;
  }
  .contacts svg { width: 14px; height: 14px; flex: none; }
</style>
</head>
<body>

<section class="card card--front" aria-label="Business card front">
  <svg class="card__art" viewBox="0 0 700 400" preserveAspectRatio="none" aria-hidden="true">
    <defs>
      <linearGradient id="bandFill" x1="0" y1="0" x2="1" y2="0.4">
        <stop offset="0" stop-color="#0f74ad"/>
        <stop offset="0.55" stop-color="#2aa7d6"/>
        <stop offset="1" stop-color="#1a8fc4"/>
      </linearGradient>
    </defs>
    <path d="M0,192 Q330,330 700,168 L700,400 L0,400 Z" fill="url(#bandFill)"/>
    <path d="M0,176 Q330,314 700,150" fill="none" stroke="var(--brand-blue)" stroke-width="4"/>
  </svg>

  <div class="brand">
    <span class="brand__dot"></span>
    <span class="brand__name">Tolverin Wealth Management</span>
  </div>

  <div class="holder">
    <h1 class="holder__name">DARREN HOLLOWAY</h1>
    <p class="holder__role">Director</p>
  </div>

  <ul class="contacts">
    <li>
      <svg viewBox="0 0 16 16" aria-hidden="true"><path d="M4 1.5l2.5 3-1.6 1.6c.9 2 2.4 3.5 4.4 4.4l1.6-1.6 3 2.5-1.6 2.6C7.5 14 2 8.5 1.4 3.1z" fill="#fff"/></svg>
      <span>+64 21 048 31176</span>
    </li>
    <li>
      <svg viewBox="0 0 16 16" aria-hidden="true"><rect x="1.5" y="3.5" width="13" height="9" fill="none" stroke="#fff" stroke-width="1.4"/><path d="M1.5 3.5L8 9l6.5-5.5" fill="none" stroke="#fff" stroke-width="1.4"/></svg>
      <span>darren@tolverinwealth.com</span>
    </li>
    <li>
      <svg viewBox="0 0 16 16" aria-hidden="true"><circle cx="8" cy="8" r="6.3" fill="none" stroke="#fff" stroke-width="1.3"/><ellipse cx="8" cy="8" rx="2.8" ry="6.3" fill="none" stroke="#fff" stroke-width="1.1"/><path d="M1.7 8h12.6" stroke="#fff" stroke-width="1.1"/></svg>
      <span>Tolverinwealthmanagment.com</span>
    </li>
  </ul>
</section>

<section class="card card--back" aria-label="Business card back">
  <div class="brand">
    <span class="brand__dot"></span>
    <span class="brand__name">Tolverin Wealth Management</span>
  </div>
</section>

</body>
</html>
```